Promotional brochure for educational consulting firm

Updates

Hi Designers!

Please do a 8.5 x 11 inch tri-fold brochure as well as a 8.5 x 11 inch half-fold brochure.  I appreciate black and white versions in addition to color.  Please take a look at my company's website for a better sense of the look and feel I am going for:  www.brightlarkco.org

Thanks!

Industry/Entity Type

Consulting

Colors
3176b5
85abd2
fcfbfd

```html
<!DOCTYPE html>
<html lang="en">
<head>
<meta charset="utf-8">
<title>Brightlark Associates – Tri-fold Brochure</title>
<link href="https://fonts.googleapis.com/css2?family=Cabin:wght@400;600;700&family=Exo+2:wght@800&family=Questrial&display=swap" rel="stylesheet">
<style>
  :root{
    --blue:#3176b5;
    --blue-deep:#1f56a8;
    --blue-soft:#85abd2;
    --paper:#fcfbfd;
    --band:#a7a8ab;
    --ink:#2a2a2a;
    --ink-mid:#3c3c3c;
    --bg:#e9eaec;
  }
  *{margin:0;padding:0;box-sizing:border-box}
  html,body{width:1200px;height:945px;overflow:hidden;background:var(--bg)}
  .brochure{
    position:absolute;left:18px;top:22px;width:1164px;height:900px;
    display:flex;background:var(--paper);
    box-shadow:0 2px 10px rgba(0,0,0,.18);
    font-family:"Cabin",sans-serif;
  }
  .panel{position:relative;width:388px;height:100%;
    background:linear-gradient(180deg,#f1f2f5 0%,var(--paper) 35%,#f3f4f7 100%);}
  .panel + .panel{border-left:1px solid #d8dae0}
  .top{position:absolute;left:0;top:0;width:100%;height:227px;text-align:center}
  .rule{position:absolute;left:0;width:100%;height:5px;background:var(--blue-soft)}
  .rule.upper{top:227px}
  .rule.lower{top:340px}
  .band{position:absolute;left:0;top:236px;width:100%;height:101px;background:var(--band);
    color:#fff;text-align:center;display:flex;flex-direction:column;justify-content:center}
  .photo{position:absolute;left:0;top:347px;width:100%;height:530px}
  .foot-bar{position:absolute;left:0;bottom:0;width:100%;height:23px;background:var(--blue)}
  .panel.middle .foot-bar{background:var(--blue-soft)}

  /* contact panel */
  .contact-title{margin-top:60px;font-weight:600;font-size:17px;letter-spacing:.5px;color:var(--blue-soft)}
  .contact-line{display:flex;align-items:center;justify-content:center;gap:5px;color:var(--ink)}
  .contact-line svg{width:14px;height:14px}
  .phone{margin-top:30px;font-weight:700;font-size:19px}
  .fax{margin-top:16px;font-size:15px}
  .web{margin-top:16px;font-family:"Questrial",sans-serif;font-size:15px}
  .person-name{font-size:25px;letter-spacing:.3px}
  .person-mail{margin-top:8px;font-size:15px;display:flex;align-items:center;justify-content:center;gap:6px}
  .pencils{background:linear-gradient(115deg,#6a3fa0 0%,#e7c23a 18%,#e25da0 34%,#d8262e 48%,#2452b8 62%,#2fa34a 78%,#7b3a1e 90%,#111 100%)}

  /* middle panel */
  .headline{position:absolute;left:0;top:400px;width:100%;text-align:center;color:var(--blue-deep)}
  .headline-lead{font-size:30px}
  .headline-figure{margin-top:6px;font-family:"Exo 2",sans-serif;font-weight:800;font-size:58px;letter-spacing:1px}

  .lockup{position:absolute;left:0;width:100%;text-align:center}
  .lockup-name{display:flex;align-items:center;justify-content:center;gap:10px;
    font-weight:700;font-size:23px;letter-spacing:.5px}
  .lockup-dot{width:20px;height:20px;border-radius:50%}
  .lockup-tag{margin-top:4px;font-size:13.5px;letter-spacing:.6px;text-transform:uppercase}
  .lockup.cover{top:140px;color:var(--blue-deep)}
  .lockup.cover .lockup-dot{background:var(--blue-deep)}
  .lockup.back{top:800px;color:var(--ink-mid)}
  .lockup.back .lockup-dot{background:var(--ink-mid)}

  /* cover panel */
  .tagline{font-size:23px;line-height:28px;padding:0 20px}
  .child{background:radial-gradient(ellipse at 55% 45%,#f2d3c4 0%,#e7b99a 22%,#f6dfe3 45%,#f7f4f6 75%,#f7f7f9 100%)}
</style>
</head>
<body>
<main class="brochure">

  <section class="panel contact">
    <div class="top">
      <h2 class="contact-title">CONTACT US</h2>
      <p class="contact-line phone">
        <svg viewBox="0 0 16 16" aria-hidden="true"><circle cx="8" cy="8" r="7" fill="none" stroke="#3176b5" stroke-width="1.2"/><path d="M6 4.5c-1 .8-1.2 2.3 0 4.3s2.6 3 3.8 2.8l.6-1.2-1.4-1-.7.6c-.6-.3-1.3-1.1-1.6-1.8l.6-.7-.8-1.5z" fill="#3176b5"/></svg>
        555.014.2270
      </p>
      <p class="contact-line fax">
        <svg viewBox="0 0 16 16" aria-hidden="true"><path d="M4 2h6v5H4z M2 7h12v6H2z" fill="none" stroke="#3176b5" stroke-width="1.2"/></svg>
        555.014.2281
      </p>
      <p class="contact-line web">
        <svg viewBox="0 0 16 16" aria-hidden="true"><circle cx="8" cy="8" r="6.5" fill="none" stroke="#3176b5" stroke-width="1.2"/><path d="M1.5 8h13M8 1.5v13M3 4.5h10M3 11.5h10" stroke="#3176b5" stroke-width=".9"/></svg>
        www.brightlarkco.org
      </p>
    </div>
    <div class="rule upper"></div>
    <div class="band">
      <p class="person-name">Maren Cole, Ed.D.</p>
      <p class="person-mail">
        <svg width="16" height="11" viewBox="0 0 16 11" aria-hidden="true"><rect x=".5" y=".5" width="15" height="10" fill="#fff"/><path d="M.5 .5l7.5 6 7.5-6" fill="none" stroke="#a7a8ab"/></svg>
        maren@brightlarkco.org
      </p>
    </div>
    <div class="rule lower"></div>
    <div class="photo pencils" role="img" aria-label="Close-up photo of sharpened coloured pencils"></div>
    <div class="foot-bar"></div>
  </section>

  <section class="panel middle">
    <div class="headline">
      <p class="headline-lead">School leadership is</p>
      <p class="headline-figure">24/7/365</p>
    </div>
    <div class="lockup back">
      <p class="lockup-name"><span class="lockup-dot"></span>BRIGHTLARK ASSOCIATES LLC</p>
      <p class="lockup-tag">Supporting Schools &amp; School Leaders</p>
    </div>
    <div class="foot-bar"></div>
  </section>

  <section class="panel cover">
    <div class="top">
      <div class="lockup cover">
        <p class="lockup-name"><span class="lockup-dot"></span>BRIGHTLARK ASSOCIATES LLC</p>
        <p class="lockup-tag">Supporting Schools &amp; School Leaders</p>
      </div>
    </div>
    <div class="rule upper"></div>
    <div class="band">
      <p class="tagline">Let’s work together to take your school to the next level of excellence.</p>
    </div>
    <div class="rule lower"></div>
    <div class="photo child" role="img" aria-label="Photo of a young girl lying on the floor holding a pencil"></div>
    <div class="foot-bar"></div>
  </section>

</main>
</body>
</html>
```